Business card design needed

Need a business card for a new Company in Melbourne called Brightway Lending Choices. This company is a Mortgage Brokering company that facilitates mainly Residential loans, but also Business and Commercial loans.
I would like something professional as I am in the finance industry.
I would like Brightway Lending font wise to be bigger than choices, with the word choices to sit below the Brightway Lending.

Industry/Entity Type

Finance

Contact Information for Business Card

Daniel Westhorpe | Lending Specialist
Brightway Lending Choices
P.O Box 517 Elmvale Vic.3071
T. +61 3 9000 4171 | F. +61 3 9000 6235| M. +61 400572904
www.brightwaylending.example

Daniel Westhorpe is a credit representative (CRN 572914)of KRVMO Pty.Ltd (Australian Credit Licence No 648502)

Requirements
Must have
• Daniel Westhorpe is a credit representative (CRN 572914)of KRVMO Pty.Ltd (Australian Credit Licence No 648502) has to sit at the bottom of the card, in the smallest readable font.

The logo to be designed is the most crucial thing for me.

```html
<!DOCTYPE html>
<html lang="en">
<head>
<meta charset="utf-8">
<title>Brightway Lending Choices – Business Card</title>
<link rel="stylesheet" href="https://fonts.googleapis.com/css2?family=Archivo+Black&family=Cabin:wght@400;600&display=swap">
<style>
  :root {
    --backdrop: #d6d7d8;
    --sky: #55d3f4;
    --silver-light: #f1f2f2;
    --silver-mid: #c4c6c7;
    --silver-dark: #8e9193;
    --ink: #1f2b33;
    --paper-white: #ffffff;
  }
  html, body {
    margin: 0;
    width: 1200px;
    height: 741px;
    overflow: hidden;
    background: var(--backdrop);
  }
  .sheet {
    width: 1200px;
    height: 741px;
    display: flex;
    align-items: center;
    justify-content: center;
    gap: 80px;
  }
  .card {
    width: 354px;
    height: 620px;
    display: block;
    box-shadow: 0 2px 6px rgba(0,0,0,0.18);
  }
  .card__sky { fill: var(--sky); }
  .wordmark {
    font-family: "Archivo Black", "Arial Black", sans-serif;
    fill: var(--ink);
  }
  .wordmark--large { font-size: 38px; }
  .wordmark--small { font-size: 18px; }
  .title-main {
    font-family: "Archivo Black", "Arial Black", sans-serif;
    font-size: 22px;
    fill: var(--ink);
    letter-spacing: 0.5px;
  }
  .title-sub {
    font-family: "Archivo Black", "Arial Black", sans-serif;
    font-size: 15px;
    fill: var(--ink);
    letter-spacing: 1px;
  }
  .contact {
    font-family: "Cabin", sans-serif;
    font-size: 11px;
    fill: var(--ink);
  }
  .holder-name {
    font-family: "Archivo Black", "Arial Black", sans-serif;
    font-size: 19px;
    fill: var(--paper-white);
  }
  .credit-note {
    font-family: "Cabin", sans-serif;
    font-size: 7.5px;
    fill: var(--ink);
  }
</style>
</head>
<body>
<main class="sheet">

  <!-- Card front -->
  <svg class="card card--front" viewBox="0 0 354 620" aria-label="Business card front">
    <defs>
      <linearGradient id="silverFront" x1="0" y1="0" x2="1" y2="1">
        <stop offset="0" stop-color="var(--silver-light)"/>
        <stop offset="0.5" stop-color="var(--silver-mid)"/>
        <stop offset="1" stop-color="var(--silver-dark)"/>
      </linearGradient>
    </defs>
    <rect class="card__base" width="354" height="620" fill="url(#silverFront)"/>
    <polygon class="card__sky" points="170,0 330,0 300,285 60,285"/>
    <polygon class="card__sky" points="40,350 300,350 180,620 0,620 0,420"/>

    <g class="wordmark wordmark--large" transform="translate(200,272) rotate(-90)">
      <text x="0" y="0">Brightway</text>
      <text x="0" y="42">Lending</text>
    </g>

    <g class="title-band">
      <text class="title-main" x="177" y="314" text-anchor="middle">BRIGHTWAY LENDING</text>
      <text class="title-sub" x="177" y="336" text-anchor="middle">CHOICES</text>
    </g>
  </svg>

  <!-- Card back -->
  <svg class="card card--back" viewBox="0 0 354 620" aria-label="Business card back">
    <defs>
      <linearGradient id="silverBack" x1="0" y1="0" x2="1" y2="1">
        <stop offset="0" stop-color="var(--silver-light)"/>
        <stop offset="0.5" stop-color="var(--silver-mid)"/>
        <stop offset="1" stop-color="var(--silver-dark)"/>
      </linearGradient>
    </defs>
    <rect class="card__base" width="354" height="620" fill="url(#silverBack)"/>
    <polygon class="card__sky" points="170,0 330,0 320,285 60,285"/>
    <polygon class="card__sky" points="40,350 300,350 180,620 0,620 0,420"/>

    <text class="wordmark wordmark--small" transform="translate(185,275) rotate(-90)">Brightway Lending</text>

    <g class="contact" transform="translate(222,275) rotate(-90)">
      <text x="0" y="0">T. +61 3 9000 4171</text>
      <text x="0" y="12">F. +61 3 9000 6235</text>
      <text x="0" y="24">M. +61 400572904</text>
      <text x="0" y="36">Email: info@brightwaylending.example</text>
      <text x="0" y="48">www.brightwaylending.example</text>
      <text x="0" y="60">Lending Specialist Brightway Lending Choices</text>
      <text x="0" y="72">P.O Box 517 Elmvale Vic.3071</text>
    </g>

    <g class="title-band">
      <text class="title-main" x="177" y="314" text-anchor="middle">BRIGHTWAY LENDING</text>
      <text class="title-sub" x="177" y="336" text-anchor="middle">CHOICES</text>
    </g>

    <g transform="translate(70,605) rotate(-90)">
      <text class="holder-name" x="0" y="0">Daniel</text>
      <text class="holder-name" x="0" y="22">Westhorpe</text>
      <text class="credit-note" x="0" y="38">Credit Representative (CRN 572914) of KRVMO Pty.Ltd</text>
      <text class="credit-note" x="0" y="48">(Australian Credit Licence No 648502)</text>
    </g>
  </svg>

</main>
</body>
</html>
```